Business Card Design for Small Electrical Contractor

I need to update my business card into something a little more modern. We are a small electrical contracting company. We service domestic and commercial places around Sydney. We have 2 logo designs at the moment. I have uploaded both and 2 different sizes to work with.

Industry/Entity Type

Business

Contact Information for Business Card

Leo Hartigan
8/21-23 Birch Rd, Kelsworth 2087
t - (02) 9381 4720
m - 0427 815 903
E - info@hartiganelx.com.au
W - hartiganelx.com.au
ABN: 42 907 551 316

Font styles to use
Sans Serif

Requirements
Must have
• I would also like to see the below fit on somewhere aswell
• - Licensed Electrician
• - Level 2 (Cat 1 & 4)
• - Domestic
• - Commercial
• - Repairs and Installations
• - Data
Nice to have
• Try and keep similar colours as logo
Should not have
• No lightning bolts or light globes. Smart and professional please.

```html
<!DOCTYPE html>
<html lang="en">
<head>
<meta charset="utf-8">
<title>Hartigan Electrical – Business Card</title>
<link rel="stylesheet" href="https://fonts.googleapis.com/css2?family=Open+Sans:wght@400;600;700&display=swap">
<style>
  :root {
    --stage: #000000;
    --card-light: #f2f2f2;
    --card-dark: #12393a;
    --ink: #173436;
    --accent: #f59f1d;
    --white: #ffffff;
  }
  * { margin: 0; padding: 0; box-sizing: border-box; }
  html, body {
    width: 1200px; height: 900px; overflow: hidden;
    background: var(--stage);
    font-family: "Open Sans", sans-serif;
  }
  .canvas { position: relative; width: 1200px; height: 900px; }

  .card { position: absolute; top: 200px; width: 310px; height: 502px; }
  .card--front {
    left: 265px; background: var(--card-light);
    border-radius: 62px 0 62px 0; color: var(--ink);
  }
  .card--back {
    left: 641px; width: 309px; background: var(--card-dark);
    border-radius: 0 62px 0 62px; color: var(--white);
  }

  .brand {
    position: absolute; font-weight: 600; font-size: 25px;
    letter-spacing: 0.2px; white-space: nowrap;
  }
  .card--front .brand { left: 38px; top: 57px; color: var(--ink); }
  .card--back .brand { left: 43px; top: 70px; color: var(--white); }

  .contact { position: absolute; left: 36px; top: 252px; font-size: 14px; line-height: 20px; }
  .contact__name { color: var(--accent); font-weight: 600; font-size: 18px; line-height: 22px; }
  .contact__role { margin-top: 0; }
  .contact__address { margin-top: 12px; margin-left: -2px; }
  .contact__abn { margin-top: 10px; margin-left: -5px; }
  .contact__abn-label { color: var(--accent); font-weight: 600; }
  .contact__list { list-style: none; margin-top: 9px; }
  .contact__list li { display: flex; align-items: center; height: 21px; }
  .contact__icon { width: 10px; height: 10px; margin-right: 8px; fill: var(--accent); flex: none; }

  .services {
    position: absolute; left: 27px; top: 335px; list-style: none;
    font-size: 14px; font-weight: 600; line-height: 24.7px;
  }
  .services li { display: flex; align-items: center; }
  .services li::before {
    content: ""; width: 8px; height: 8px; border-radius: 50%;
    background: var(--accent); margin-right: 8px;
  }
</style>
</head>
<body>
<div class="canvas">
  <section class="card card--front">
    <div class="brand">Hartigan Electrical</div>
    <div class="contact">
      <p class="contact__name">Leo Hartigan</p>
      <p class="contact__role">Licensed Electrician</p>
      <p class="contact__address">8/21-23 Birch Rd,<br>Kelsworth 2087</p>
      <p class="contact__abn"><span class="contact__abn-label">ABN:</span> 42 907 551 316</p>
      <ul class="contact__list">
        <li><svg class="contact__icon" viewBox="0 0 10 10"><path d="M2 0.5l1.6 2.2-1 1a5 5 0 0 0 3.7 3.7l1-1 2.2 1.6-1 1.6C4.5 9.6 0.4 5.5 0.4 1.5z"/></svg>(02) 9381 4720</li>
        <li><svg class="contact__icon" viewBox="0 0 10 10"><path d="M2.5 0h5v10h-5z M3.5 1v7h3V1z"/></svg>0427 815 903</li>
        <li><svg class="contact__icon" viewBox="0 0 10 10"><path d="M0 2h10v6H0z"/><path d="M0 2l5 3.5L10 2" stroke="#f2f2f2" stroke-width="0.8" fill="none"/></svg>info@hartiganelx.com.au</li>
        <li><svg class="contact__icon" viewBox="0 0 10 10"><circle cx="5" cy="5" r="5"/><path d="M0 5h10M5 0c-2.5 3-2.5 7 0 10M5 0c2.5 3 2.5 7 0 10" stroke="#f2f2f2" stroke-width="0.7" fill="none"/></svg>hartiganelx.com.au</li>
      </ul>
    </div>
  </section>

  <section class="card card--back">
    <div class="brand">Hartigan Electrical</div>
    <ul class="services">
      <li>Domestic</li>
      <li>Commercial</li>
      <li>Repairs and Installations</li>
      <li>Data</li>
    </ul>
  </section>
</div>
</body>
</html>
```